Marketplace Web Re-design overhaul @quarrynest

Hi,
We are currently in production with a website that is getting some mixed feedback about visual appeal and usability. We are using a responsive design and need to stay true to the logo colours and other marketing collateral we have in place. I will provide a brochure with the colour palate we use for some guidance. If you can please help us design something fresh and modern to communicate the essence of our company. The brochure will be a good summary of what we do and who we are targeting as customers. Our current website can be found at www.quarrynest.com. If there is any questions, please let me know.

Target Market(s)

Contractors and Corporate Companies

Industry/Entity Type

Information Technology

Number of Pages Required

4 page

Requirements
Must have
• Must have a complete new visual look, including
• 1. Images
• 2. Background colour scheme overhaul (not black)
• 3. re-design of the layout but keep to similar page breakdowns
Nice to have
• Some of the pages are a bit wordy, happy to have suggestions on how to reduce.
• Would be great if we can integrate the Plumb.ON! blog page to the Quarrynest page?
• This is some feedback a fellow UX designer provided to improve our CRO
• First off when you land on the home page, who is your audience? Are you everything to everyone? Even after watching the video (https://www.vidmarrow.net/watch?v=q7RtPe3LwZ0), I do not know what markets you service or who this app will be for.
• Your main headline and paragraph above the fold I find unnecessarily wordy and an overuse of 'buzzwords' . Perhaps you could look at appealing to the lowest common denominator and make it very simple and put it all into a simple sentence.
• The main hero image to the right of the headline offers no emotional pull at all. I'm assuming it's just a screenshot of your dashboard? Personally, I would be looking at using a person's image in that space.
• Also in this space, increase the size of your 'register' button. On the topic of your register button, you have it in different colours. Green in header, and red in content. Make it the same colour, and don't use that colour again on the site. That colour is to become your call to action (CTA) colour. Understandably you'll have three different colours for the account type, and again, don't use these colours anywhere else on the site.
• The registration area where the three account types are where you choose which one suits you, it's extremely busy with background images and heavy use of text. If you were my client, I would be advising you to ditch the bg image (including the Zelo shot), keeping the text, making the register icons much bigger. Perhaps instead of bg images, use a solid colour for each (green, orange, red). I'm highly confident this change will make a massive difference in your sign up rate.
Should not have
• Please keep to the fonts used on the original website
• Keep to the colour provided on the company brochure for guidance.

```html
<!DOCTYPE html>
<html lang="en">
<head>
<meta charset="utf-8">
<title>Quarrynest – About Us</title>
<link href="https://fonts.googleapis.com/css2?family=Arimo:wght@400;700&display=swap" rel="stylesheet">
<style>
:root{
  --green:#3fb54a;
  --green-soft:#6fcf7a;
  --footer:#42a84c;
  --footer-deep:#38963f;
  --ink:#2b2b2b;
  --body:#555a60;
  --muted:#777;
  --mist:#e9ebef;
  --white:#fff;
}
*{margin:0;padding:0;box-sizing:border-box}
html,body{width:1200px;height:2323px;overflow:hidden}
body{font-family:"Arimo",Arial,sans-serif;color:var(--ink);background:var(--white);position:relative}
.page{position:relative;width:1200px;height:2323px}

/* hero */
.hero{position:absolute;left:0;top:0;width:1200px;height:653px;
  background:radial-gradient(ellipse at 30% 45%,#7c8388 0%,#4e5459 40%,#2c3034 80%,#1e2124 100%)}
.nav{position:absolute;left:0;top:0;width:1200px;height:47px;border-bottom:1px solid rgba(255,255,255,.15)}
.brand{position:absolute;left:160px;top:14px;display:flex;align-items:center;gap:6px;color:var(--white);font-size:17px}
.brand-dot{width:14px;height:14px;border-radius:50%;background:var(--green)}
.nav-links{position:absolute;top:18px;left:0;list-style:none;font-size:11px;color:var(--white)}
.nav-links li{position:absolute;white-space:nowrap}
.nav-links .active::after{content:"";position:absolute;left:-6px;right:-6px;top:26px;height:3px;background:var(--green)}
.account{position:absolute;top:18px;left:972px;font-size:10px;color:var(--white)}
.account .register{color:var(--green);margin-left:8px}
.hero-copy{position:absolute;left:290px;top:282px;width:620px;text-align:center;color:var(--white);font-size:18px;line-height:22px}
.join{position:absolute;left:545px;top:398px;width:108px;height:33px;background:var(--green);color:var(--white);font-size:13px;line-height:33px;text-align:center;border-radius:2px}

/* about */
.section-title{position:absolute;left:0;width:1200px;text-align:center;font-size:23px;font-weight:400;letter-spacing:1.5px;color:var(--ink)}
.section-title::after{content:"";display:block;width:126px;height:3px;background:var(--green);margin:12px auto 0}
.about-title{top:690px}
.about-copy{position:absolute;left:160px;top:771px;width:884px;font-size:9.4px;line-height:12.3px;color:var(--body)}
.about-copy p{margin-bottom:9px}
.team-bg{position:absolute;left:0;top:1416px;width:1200px;height:655px;background:var(--mist)}
.team-photo{position:absolute;left:0;top:948px}
.photo-caption{position:absolute;left:160px;top:1436px;width:540px;font-size:8.6px;line-height:11px;color:var(--white)}

/* team */
.team-title{top:1519px}
.avatar{position:absolute;border-radius:50%;background:radial-gradient(circle at 50% 40%,#b9bcc0,#7d8186);border:3px solid var(--white)}
.tag{position:absolute;background:var(--white);text-align:center;padding-top:6px;box-shadow:0 1px 2px rgba(0,0,0,.08)}
.tag .name{display:block;color:var(--green);font-size:13px;line-height:15px}
.tag .role{display:block;color:var(--muted);font-size:8px;line-height:11px}
.tag::before{content:"";position:absolute;left:-6px;top:13px;border:6px solid transparent;border-left:0;border-right-color:var(--white)}
.profile-card{position:absolute;left:906px;top:1653px;width:127px;height:174px;background:var(--green-soft);color:var(--white);text-align:center;padding:7px 10px}
.profile-card .name{font-size:13px;line-height:16px}
.profile-card .role{font-size:8px;margin-bottom:10px;border-bottom:1px solid rgba(255,255,255,.5);padding-bottom:5px}
.profile-card .bio{font-size:8px;line-height:10px;text-align:center}
.card-social{position:absolute;left:0;bottom:10px;width:100%;display:flex;justify-content:center;gap:9px}
.dot{width:8px;height:8px;border-radius:50%;background:var(--white)}

/* footer */
.footer{position:absolute;left:0;top:2071px;width:1200px;height:208px;background:var(--footer);color:var(--white)}
.footer-brand{position:absolute;left:206px;top:40px;display:flex;align-items:center;gap:6px;font-size:17px}
.footer-about{position:absolute;left:206px;top:81px;width:200px;font-size:10px;line-height:12px}
.footer-col h4{font-weight:400;font-size:11px;letter-spacing:.5px;padding-bottom:10px;border-bottom:1px solid rgba(255,255,255,.4)}
.sitemap{position:absolute;left:488px;top:41px;width:204px}
.sitemap-lists{display:flex;gap:44px;margin-top:12px}
.sitemap ul{list-style:none;font-size:10px;line-height:18px;width:68px}
.newsletter{position:absolute;left:788px;top:41px;width:204px}
.newsletter p{font-size:10px;margin-top:16px}
.email{margin-top:20px;height:27px;border:1px solid rgba(255,255,255,.8);display:flex;align-items:center;justify-content:space-between;padding:0 10px;font-size:10px}
.bottom-bar{position:absolute;left:0;top:2279px;width:1200px;height:44px;background:var(--footer-deep);color:var(--white);font-size:9px}
.copyright{position:absolute;left:206px;top:17px}
.bar-social{position:absolute;left:926px;top:17px;display:flex;gap:10px}
</style>
</head>
<body>
<div class="page">

<header class="hero" role="img" aria-label="Photo of hands typing on a laptop, dark toned">
  <nav class="nav">
    <div class="brand"><span class="brand-dot"></span>quarrynest</div>
    <ul class="nav-links">
      <li style="left:378px">HOME</li>
      <li style="left:438px">HOW IT WORKS</li>
      <li class="active" style="left:546px">ABOUT US</li>
      <li style="left:630px">OUR PARTNERS</li>
      <li style="left:740px">FAQ</li>
      <li style="left:790px">BLOG</li>
    </ul>
    <div class="account">Log in<span class="register">Register</span></div>
  </nav>
  <p class="hero-copy">Finally a platform where companies can connect directly with professional contractors. No agencies, no hidden fees, no fuss. Quarrynest believes that contractors should be paid a fair market rate for their services and employers should be able to find contractors cheaper than they do today.</p>
  <div class="join">JOIN NOW</div>
</header>

<h2 class="section-title about-title">ABOUT US</h2>
<div class="about-copy">
  <p>Co-Founders Marisol and Dario initially created Quarrynest to answer an important capability that was missing in all the contractor / freelance management systems in the market today – "Contingent Skills Available". Additionally they did not want a jobs board, nor want to create yet another system for contractors to maintain for work, however still needed to enable connectivity for the demand and supply.</p>
  <p>Marisol is a technologist and returned to the workforce after having kids, she was challenged for part-time work preferring a flexible schedule. Joining the recruitment industry it was thriving but she was consistently frustrated in trying to match available contractors for her clients and the inefficiencies associated with successfully connecting contractors with her clients. The outdated system were not reflective of who was available, having to place Postmarrow ads and lots of calls &amp; emails to source the right candidates, taking longer time to fill and costing money which was generally paid by the client. The shortage of skills and visibility was a growing problem.</p>
  <p>Dario is in business and was also frustrated in not being able to source contractors with specific skills and experience within a timeframe and dealt with a number of agencies with very little success and when successful, was paying a premium for contractors. Furthermore, contractors wanted to be empowered with being in control of their valuable assets: Their time and their skills! Both felt that there was a better way to leverage technology to bridge this missing link so Quarrynest was born!</p>
  <p style="width:520px">In addition to the "availability" functionality, they are committed to improving the transparency and fairness in the transaction process so companies know the rate they are paying for contractors based on the rate the contractor is seeking. Since its inception, Quarrynest has added more functionality requested by companies &amp; contractors using it and is continually improving and refining capability.</p>
</div>

<div class="team-bg"></div>
<svg class="team-photo" width="1200" height="530" viewBox="0 948 1200 530" role="img" aria-label="Group photo of the extended Quarrynest team standing in a blue office">
  <defs>
    <linearGradient id="office" x1="0" y1="0" x2="1" y2="1">
      <stop offset="0" stop-color="#6fa6d6"/>
      <stop offset=".5" stop-color="#3f6f9c"/>
      <stop offset="1" stop-color="#2a3f57"/>
    </linearGradient>
  </defs>
  <polygon points="0,1014 682,1014 715,948 1200,948 1200,1416 758,1416 713,1478 0,1478" fill="url(#office)"/>
</svg>
<p class="photo-caption">Meet our extended Quarrynest family: Piers Calloway (Advisor), Neil Hardwick (COO and Advisory Board Member), Leo Marchetti (Advisory Board Member), Dario Castellan (CTO &amp; Co-Founder), Marisol Venner (CEO &amp; Co-Founder), Grant Ellery (Advisory Board Member), Victor Sammut (Advisory Board Member) and Owen Barrick (Advisor)</p>

<h2 class="section-title team-title">MEET OUR TEAM</h2>

<div class="avatar" role="img" aria-label="Portrait of Marisol Venner" style="left:263px;top:1607px;width:146px;height:146px"></div>
<div class="tag" style="left:393px;top:1633px;width:146px;height:36px"><span class="name">Marisol Venner</span><span class="role">CEO &amp; Co-Founder</span></div>

<div class="avatar" role="img" aria-label="Portrait of Dario Castellan" style="left:542px;top:1628px;width:124px;height:124px"></div>
<div class="tag" style="left:647px;top:1659px;width:112px;height:37px"><span class="name">Dario Castellan</span><span class="role">CTO &amp; Co-Founder</span></div>

<div class="avatar" role="img" aria-label="Portrait of Leo Marchetti" style="left:803px;top:1631px;width:112px;height:112px"></div>
<div class="profile-card">
  <div class="name">Leo Marchetti</div>
  <div class="role">Advisory Board Member</div>
  <p class="bio">Lorem Ipsum is simply dummy text of the printing and typesetting industry. Lorem Ipsum has been the industry's standard dummy text.Printer took a galley of type and scra abled it to make. Lorem Ipsum .</p>
  <div class="card-social"><span class="dot"></span><span class="dot"></span><span class="dot"></span><span class="dot"></span></div>
</div>

<div class="avatar" role="img" aria-label="Portrait of Grant Ellery" style="left:163px;top:1754px;width:108px;height:108px"></div>
<div class="tag" style="left:262px;top:1785px;width:122px;height:38px"><span class="name">Grant Ellery</span><span class="role">Advisory Board Member</span></div>

<div class="avatar" role="img" aria-label="Portrait of Neil Hardwick" style="left:410px;top:1752px;width:118px;height:118px"></div>
<div class="tag" style="left:514px;top:1808px;width:152px;height:37px"><span class="name">Neil Hardwick</span><span class="role">COO &amp; Advisory Board Member</span></div>

<div class="avatar" role="img" aria-label="Portrait of Idris Farahani" style="left:676px;top:1743px;width:124px;height:124px"></div>
<div class="tag" style="left:790px;top:1768px;width:124px;height:37px"><span class="name">Idris Farahani</span><span class="role">Senior Developer</span></div>

<div class="avatar" role="img" aria-label="Portrait of Arun Desai" style="left:299px;top:1870px;width:114px;height:114px"></div>
<div class="tag" style="left:406px;top:1933px;width:93px;height:37px"><span class="name">Arun Desai</span><span class="role">Developer</span></div>

<div class="avatar" role="img" aria-label="Portrait of Tarek Haddad" style="left:530px;top:1872px;width:148px;height:148px"></div>
<div class="tag" style="left:658px;top:1963px;width:108px;height:37px"><span class="name">Tarek Haddad</span><span class="role">Technical Expert</span></div>

<div class="avatar" role="img" aria-label="Portrait of Victor Sammut" style="left:805px;top:1872px;width:102px;height:102px"></div>
<div class="tag" style="left:898px;top:1887px;width:118px;height:37px"><span class="name">Victor Sammut</span><span class="role">Advisory Board Member</span></div>

<footer class="footer">
  <div class="footer-brand"><span class="brand-dot" style="background:#fff"></span>quarrynest</div>
  <p class="footer-about">Lorem Ipsum is simply dummy text of the printing and typesetting industry. Lorem Ipsum has been the industry's standard dummy</p>
  <div class="footer-col sitemap">
    <h4>SITEMAP</h4>
    <div class="sitemap-lists">
      <ul><li>Home</li><li>About Us</li><li>Our Partner</li><li>FAQ</li><li>Blog</li></ul>
      <ul><li>Term Of Use</li><li>Privacy Policy</li><li>Contact Us</li></ul>
    </div>
  </div>
  <div class="footer-col newsletter">
    <h4>NEWSLETTER</h4>
    <p>Subscribe to our newsletter.</p>
    <div class="email"><span>Email address</span>
      <svg width="12" height="8" viewBox="0 0 12 8"><path d="M0 4h10M7 1l3 3-3 3" stroke="#fff" stroke-width="1.3" fill="none"/></svg>
    </div>
  </div>
</footer>
<div class="bottom-bar">
  <span class="copyright">© Copyright 2016 Quarrynest</span>
  <div class="bar-social"><span class="dot"></span><span class="dot"></span><span class="dot"></span><span class="dot"></span></div>
</div>

</div>
</body>
</html>
```